Real Estate Business Folders, Business Cards, Envelopes & Letterhead

Im looking for trendy, modern & professional design concepts for my business folder that will be used for real estate documents and property report presentations. I'm also looking for Business card designs, envelopes and letterhead with a similar theme. I have a logo already and I would like the logo colors to be incorporated in the design concepts.

Target Market(s)

Real Estate Investors, Banks, Financial Institutions

Industry/Entity Type

Real Estate

Colors
0455a3
959595
d3d3d3
848484

Requirements
Must have
• Trendy Modern, High Class look. Please include logo and colors and incorporate some silver or metallic.
• Business Address: 4127 Corvello Blvd ste 208-310
• N. Las Vegas, NV 89084
• Phone: 702-555-0187
• Fax : 702-555-0142
• Email: info@brookmerecastlesales.example
• Website: BrookmereCastleSales.example

```html
<!DOCTYPE html>
<html lang="en">
<head>
<meta charset="utf-8">
<title>Brookmere Castle Sales – Business Card</title>
<link href="https://fonts.googleapis.com/css2?family=Roboto:wght@400;500;700&display=swap" rel="stylesheet">
<style>
  :root {
    --brand-blue: #0455a3;
    --silver: #a4a4a6;
    --silver-light: #d3d3d3;
    --text-grey: #4a4a4a;
    --title-grey: #959595;
    --page: #2b2b2b;
    --white: #ffffff;
  }
  * { box-sizing: border-box; margin: 0; padding: 0; }
  html, body { width: 1200px; height: 960px; overflow: hidden; }
  body {
    background: var(--page);
    font-family: "Roboto", Arial, sans-serif;
    position: relative;
  }
  .card {
    position: absolute;
    left: 300px;
    width: 600px;
    height: 343px;
    box-shadow: 0 10px 30px rgba(0,0,0,.45);
  }
  /* Back side */
  .card-back {
    top: 90px;
    background: var(--brand-blue);
    color: var(--white);
    display: flex;
    flex-direction: column;
    align-items: center;
    justify-content: center;
  }
  .back-brand {
    display: flex;
    align-items: center;
    gap: 14px;
    font-size: 30px;
    font-weight: 500;
    margin-top: 10px;
    white-space: nowrap;
  }
  .back-brand .mark { width: 22px; height: 22px; background: var(--white); }
  .back-url {
    position: absolute;
    bottom: 44px;
    left: 0; right: 0;
    text-align: center;
    font-size: 15px;
    letter-spacing: .2px;
  }
  /* Front side */
  .card-front {
    top: 520px;
    background: var(--white);
    overflow: hidden;
  }
  .front-brand {
    position: absolute;
    left: 34px;
    top: 152px;
    width: 268px;
    display: flex;
    align-items: center;
    gap: 9px;
    color: var(--brand-blue);
    font-size: 21px;
    font-weight: 500;
    white-space: nowrap;
  }
  .front-brand .mark { width: 14px; height: 14px; background: var(--brand-blue); flex: none; }
  .divider {
    position: absolute;
    left: 320px;
    top: 40px;
    width: 1px;
    height: 230px;
    background: linear-gradient(to bottom, transparent, var(--silver-light) 20%, var(--silver-light) 80%, transparent);
  }
  .contact {
    position: absolute;
    left: 345px;
    top: 48px;
    right: 12px;
  }
  .contact .name {
    color: var(--brand-blue);
    font-size: 24px;
    font-weight: 700;
    line-height: 1;
  }
  .contact .role {
    color: var(--title-grey);
    font-size: 15px;
    margin-top: 3px;
  }
  .contact .address {
    color: var(--text-grey);
    font-size: 13px;
    line-height: 1.4;
    margin-top: 16px;
  }
  .contact ul { list-style: none; margin-top: 12px; }
  .contact li {
    display: flex;
    align-items: center;
    gap: 8px;
    color: var(--text-grey);
    font-size: 13px;
    line-height: 1.55;
    white-space: nowrap;
  }
  .contact li svg { width: 12px; height: 12px; fill: var(--brand-blue); flex: none; }
  .bottom-band {
    position: absolute;
    left: 0; right: 0; bottom: 0;
    height: 11px;
    display: flex;
  }
  .band-blue-left { width: 44%; background: var(--brand-blue); }
  .band-silver { width: 31%; background: linear-gradient(to bottom, #c4c4c6, var(--silver)); margin-top: -3px; }
  .band-blue-right { flex: 1; background: var(--brand-blue); }
</style>
</head>
<body>

  <section class="card card-back">
    <div class="back-brand"><span class="mark"></span>Brookmere Castle Sales</div>
    <p class="back-url">www.BrookmereCastleSales.example</p>
  </section>

  <section class="card card-front">
    <div class="front-brand"><span class="mark"></span>Brookmere Castle Sales</div>
    <div class="divider"></div>
    <div class="contact">
      <p class="name">DANIEL REYES</p>
      <p class="role">CEO/FOUNDER</p>
      <p class="address">4127 Corvello Blvd ste 208-310<br>N. Las Vegas, NV 89084</p>
      <ul>
        <li>
          <svg viewBox="0 0 24 24" aria-hidden="true"><path d="M6.6 10.8a15 15 0 0 0 6.6 6.6l2.2-2.2c.3-.3.7-.4 1-.2 1.1.4 2.3.6 3.6.6.6 0 1 .4 1 1V20c0 .6-.4 1-1 1A17 17 0 0 1 3 4c0-.6.4-1 1-1h3.5c.6 0 1 .4 1 1 0 1.3.2 2.5.6 3.6.1.3 0 .7-.2 1z"/></svg>
          702-555-0187
        </li>
        <li>
          <svg viewBox="0 0 24 24" aria-hidden="true"><path d="M6 2h12v6H6zM4 9h16a2 2 0 0 1 2 2v6h-4v5H6v-5H2v-6a2 2 0 0 1 2-2zm4 8v3h8v-3z"/></svg>
          702-555-0142
        </li>
        <li>
          <svg viewBox="0 0 24 24" aria-hidden="true"><path d="M2 5h20v14H2zm2 2v.5l8 5 8-5V7z"/></svg>
          info@brookmerecastlesales.example
        </li>
        <li>
          <svg viewBox="0 0 24 24" aria-hidden="true"><circle cx="12" cy="12" r="10"/></svg>
          BrookmereCastleSales.example
        </li>
      </ul>
    </div>
    <div class="bottom-band">
      <span class="band-blue-left"></span>
      <span class="band-silver"></span>
      <span class="band-blue-right"></span>
    </div>
  </section>

</body>
</html>
```